Thai Takeaway Menu Design

I need a menu re-design for a thai takeaway/restaurant in australia.

Please use content from the existing menu
http://www.platterwink.example/u/menu/7302918?p=1

I'd like to emphasise on
1 - free delivery for order over $40
2 - gluten free and vegetatian option available on most meal (however you want to word it - not fuss)

*remove (the banner order online and save $10)

I'm happy to change the whole concept & design. I particularly like rustic, raw look more than moden ones. Does not need to be flowery or anything like current one :)

Industry/Entity Type

Restaurant

```html
<!DOCTYPE html>
<html lang="en">
<head>
<meta charset="utf-8">
<title>Thai Takeaway Menu</title>
<link rel="stylesheet" href="https://fonts.googleapis.com/css2?family=Source+Sans+3:wght@400;600&display=swap">
<style>
  :root {
    --cream: #fdf8d9;
    --edge: #eadfc2;
    --red: #d7000f;
    --ink: #2a1a10;
    --white: #ffffff;
  }
  * { box-sizing: border-box; margin: 0; padding: 0; }
  html, body { width: 1200px; height: 849px; overflow: hidden; background: var(--cream); }
  body { font-family: "Source Sans 3", "Myriad Pro", Arial, sans-serif; color: var(--ink); }
  .menu { position: relative; width: 1200px; height: 849px; background: var(--cream); }
  .menu__edge {
    position: absolute; inset: 0;
    border: 14px solid var(--edge);
    pointer-events: none;
  }
  .section { position: absolute; width: 302px; }
  .section__title {
    height: 44px; background: var(--red); color: var(--white);
    font-size: 32px; font-weight: 400; line-height: 44px; padding-left: 8px;
  }
  .dishes { list-style: none; margin-top: 14px; font-size: 15.5px; line-height: 19px; }
  .dish { display: grid; grid-template-columns: 1fr 58px; align-items: end; }
  .dish__price { text-align: left; }
  .col-left { left: 23px; }
  .col-mid { left: 422px; }
  .col-right { left: 819px; }
  .notice {
    position: absolute; left: 422px; top: 755px; width: 699px; height: 71px;
    background: var(--red); color: var(--white);
    font-size: 20px; line-height: 21px; text-align: center; padding-top: 4px;
  }
  .notice__delivery { font-weight: 600; }
</style>
</head>
<body>
<main class="menu">
  <div class="menu__edge" role="img" aria-label="Decorative diamond pattern border framing the menu"></div>

  <section class="section col-left" style="top:24px">
    <h2 class="section__title">Entree</h2>
    <ul class="dishes">
      <li class="dish"><span>Spring Rolls *(4)</span><span class="dish__price">$6.00</span></li>
      <li class="dish"><span>Satay Chicken (4)</span><span class="dish__price">$6.00</span></li>
      <li class="dish"><span>Fish Cakes (4)</span><span class="dish__price">$6.00</span></li>
      <li class="dish"><span>Dim Sum (4)</span><span class="dish__price">$6.00</span></li>
      <li class="dish"><span>Duck Rice Paper Rolls *(2)</span><span class="dish__price">$6.00</span></li>
      <li class="dish"><span>Papaya Salad</span><span class="dish__price">$6.00</span></li>
      <li class="dish"><span>Tofu / with Peanut Sauce *</span><span class="dish__price">$6.00</span></li>
    </ul>
  </section>

  <section class="section col-left" style="top:245px">
    <h2 class="section__title">Soup</h2>
    <ul class="dishes">
      <li class="dish"><span>Tom Yum Prawn *</span><span class="dish__price">$7.00</span></li>
      <li class="dish"><span>Tom Kha Chicken *</span><span class="dish__price">$7.00</span></li>
    </ul>
  </section>

  <section class="section col-left" style="top:362px">
    <h2 class="section__title">Curry</h2>
    <ul class="dishes">
      <li class="dish"><span>Green Curry Chicken *</span><span class="dish__price">$12.90</span></li>
      <li class="dish"><span>Panang Chicken *</span><span class="dish__price">$12.90</span></li>
      <li class="dish"><span>Red Curry Beef *</span><span class="dish__price">$12.90</span></li>
      <li class="dish"><span>Massaman Beef Curry</span><span class="dish__price">$12.90</span></li>
      <li class="dish"><span>Red Duck Curry</span><span class="dish__price">$16.90</span></li>
      <li class="dish"><span>Yellow Curry Chicken *</span><span class="dish__price">$12.90</span></li>
      <li class="dish"><span>Yellow Curry Prawn</span><span class="dish__price">$16.90</span></li>
    </ul>
  </section>

  <section class="section col-left" style="top:584px">
    <h2 class="section__title">Vegetable</h2>
    <ul class="dishes">
      <li class="dish"><span>Mixed Vegetables *</span><span class="dish__price">$10.50</span></li>
      <li class="dish"><span>Steamed Veg / with Peanut Sauce *</span><span class="dish__price">$10.50</span></li>
    </ul>
  </section>

  <section class="section col-left" style="top:710px">
    <h2 class="section__title">Beef</h2>
    <ul class="dishes">
      <li class="dish"><span>Beef / with Oyster Sauce *</span><span class="dish__price">$12.90</span></li>
      <li class="dish"><span>Grilled Beef salad *</span><span class="dish__price">$12.90</span></li>
    </ul>
  </section>

  <section class="section col-mid" style="top:24px">
    <h2 class="section__title">Chicken</h2>
    <ul class="dishes">
      <li class="dish"><span>Laab Chicken *</span><span class="dish__price">$12.90</span></li>
      <li class="dish"><span>Chicken / with Sweet Basil *</span><span class="dish__price">$12.90</span></li>
      <li class="dish"><span>Chicken / with Cashew Nuts *</span><span class="dish__price">$12.90</span></li>
      <li class="dish"><span>Grilled Chicken / with Salad</span><span class="dish__price">$12.90</span></li>
      <li class="dish"><span>Southern Style Fried Chicken</span><span class="dish__price">$12.90</span></li>
    </ul>
  </section>

  <section class="section col-mid" style="top:202px">
    <h2 class="section__title">Pork</h2>
    <ul class="dishes">
      <li class="dish"><span>Sweet &amp; Sour Pork *</span><span class="dish__price">$12.90</span></li>
      <li class="dish"><span>Garlic Pork</span><span class="dish__price">$12.90</span></li>
      <li class="dish"><span>Crispy Pork / with Asian Greens *</span><span class="dish__price">$12.90</span></li>
    </ul>
  </section>

  <section class="section col-mid" style="top:345px">
    <h2 class="section__title">Duck</h2>
    <ul class="dishes">
      <li class="dish"><span>Roast Duck / with Veg &amp; Gravy</span><span class="dish__price">$16.90</span></li>
      <li class="dish"><span>Duck / Sweet Basil</span><span class="dish__price">$16.90</span></li>
      <li class="dish"><span>Honey Glazed Duck / with Veg</span><span class="dish__price">$16.90</span></li>
    </ul>
  </section>

  <section class="section col-mid" style="top:477px">
    <h2 class="section__title">Seafood</h2>
    <ul class="dishes">
      <li class="dish"><span>Garlic Prawn</span><span class="dish__price">$16.90</span></li>
      <li class="dish"><span>Tamarind Prawn</span><span class="dish__price">$16.90</span></li>
      <li class="dish"><span>Laab Fish</span><span class="dish__price">$16.90</span></li>
      <li class="dish"><span>Crispy Fish / with Sweet Chilli Salsa</span><span class="dish__price">$16.90</span></li>
      <li class="dish"><span>Chilli &amp; Lime Calamari Salad</span><span class="dish__price">$16.90</span></li>
      <li class="dish"><span>Salt &amp; Pepper Calamari</span><span class="dish__price">$16.90</span></li>
      <li class="dish"><span>Spicy Seafood</span><span class="dish__price">$16.90</span></li>
      <li class="dish"><span>Crispy Barramundi / with<br>Green Mango Salad (seasonal)</span><span class="dish__price">$22.90</span></li>
      <li class="dish"><span>Soft Shaell Chilli Crab</span><span class="dish__price">$22.90</span></li>
    </ul>
  </section>

  <section class="section col-right" style="top:24px">
    <h2 class="section__title">Noodle</h2>
    <ul class="dishes">
      <li class="dish"><span>Pad Thai *</span><span class="dish__price">$12.50</span></li>
      <li class="dish"><span>Pad Thai Prawn</span><span class="dish__price">$16.90</span></li>
      <li class="dish"><span>Drunken Noodle *</span><span class="dish__price">$12.50</span></li>
      <li class="dish"><span>Pad See Eew*</span><span class="dish__price">$12.50</span></li>
      <li class="dish"><span>Beef Nodle Soup</span><span class="dish__price">$12.50</span></li>
      <li class="dish"><span>Seafood Laska</span><span class="dish__price">$16.90</span></li>
    </ul>
  </section>

  <section class="section col-right" style="top:224px">
    <h2 class="section__title">Rice</h2>
    <ul class="dishes">
      <li class="dish"><span>Rice (S)</span><span class="dish__price">$2.50</span></li>
      <li class="dish"><span>Rice (L)</span><span class="dish__price">$3.50</span></li>
      <li class="dish"><span>Coconut Rice (S)</span><span class="dish__price">$4.50</span></li>
      <li class="dish"><span>Coconut Rice (L)</span><span class="dish__price">$5.50</span></li>
      <li class="dish"><span>Fried Rice</span><span class="dish__price">$10.50</span></li>
      <li class="dish"><span>Roti Bread</span><span class="dish__price">$3.50</span></li>
    </ul>
  </section>

  <section class="section col-right" style="top:422px">
    <h2 class="section__title">Dessert</h2>
    <ul class="dishes">
      <li class="dish"><span>Black Sticky Rice / with<br>Coconut Cream</span><span class="dish__price">$4.50</span></li>
      <li class="dish"><span>Tapioca Pudding / with Lychee</span><span class="dish__price">$4.50</span></li>
    </ul>
  </section>

  <section class="section col-right" style="top:560px">
    <h2 class="section__title">Drinks</h2>
    <ul class="dishes">
      <li class="dish"><span>Kola, Diet Kola, Orango,<br>Limefizz, Zesta - 375ml</span><span class="dish__price">$2.00</span></li>
      <li class="dish"><span>Kola, Orango, Limefizz - 1.25l</span><span class="dish__price">$4.50</span></li>
      <li class="dish"><span>Orange Juice / Apple Juice</span><span class="dish__price">$3.50</span></li>
      <li class="dish"><span>Ginger Beer</span><span class="dish__price">$3.50</span></li>
    </ul>
  </section>

  <p class="notice"><span class="notice__delivery">Free delivery for orders over $40</span><br>* Available as Vegitarian Option on Request.<br>Gluten Free options also available, please ask for details</p>
</main>
</body>
</html>
```